Marlow Landscaping Landing Page

I require a landing page for my landscaping business.

My business plan revolves around hooking clients with weeding services. Not lawn herbicide sprays, but actual hand weeding and bed maintenance. I've found my niche as most people do not want to do this kind of work. From there I often upsell clients into actual hardscaping or softscaping.

I like things to be clean, concise, and to the point. Not overly flashy, but not so minimal that that it's boring. My logo is a very good example of what I like.

The business is LGBTQ owned and operated. I do not broadcast this but I feel the logo itself, along with the name is usually enough to tip people into assumption. I'm not opposed to color, but I do not want the page to scream "gay". My favourite color is yellow...

I used to be a door to door salesman so I'm doing something different where I want to do all my selling in my first meeting with the client. With this said I do not need a section for "work pictures", as I have photos of my work on my tablet, which I show the client during the consultation.

Ideally i'd like my web site to actually be just a landing page. I'd like room for all the following information within the page;

- description of services;
Weeding of Perennial and Flower Beds
Selective Pruning of Trees and Shrubs
Hedging
Landscape Construction
Landscape Design
Total Lawn Treatment Plans
Landscape Pest Control

- contact information, phone, email
Gerald Hanswick
204-731-4426
ger.hanswick@brelvanyard.com

- "free estimates" somewhere on the page that is either led to by the eye, or very easy to notice and see

- and my slogan which is "dependable, reliable, consistent"

- room for a link to my future ratewell account so they can see reviews from real people

- My Logo present

Any or all of these can be custom made graphics or simply text, whatever looks best

I do not want people to have to search for information throughout. Design it in such a way that either the eye flows naturally from one piece of information to the other, or that it's all compartmentalized neatly enough that everything is easy to find.

As I am a landscape and outdoor maintenance service I'm no opposed to images such as flowers, trees, landscaping, etc being present. However please note that my main focus and source of income comes from weeding services, everything else is bonus cash.

Many of my clients are extremely wealthy individuals who pay over $1000 for the season for me just to show up and pull weeds. So making the website appeal to wealthy people as opposed to the average joe is paramount.

I do not cut grass. Please do not have any indication on the website, either through writing or graphics that implies that I cut grass. There are enough companies doing that.

Target Market(s)

Wealthy, often elderly individuals.

Industry/Entity Type

Landscape Gardening

Coding

Coded - Design and coding required

Number of Pages Required

1 page

Font styles to use
Sans Serif

Colors

Designer to choose colors to be used in the design.

Requirements
Must have
• - description of services;
• Weeding of Perennial and Flower Beds
• Selective Pruning of Trees and Shrubs
• Hedging
• Landscape Construction
• Landscape Design
• Total Lawn Treatment Plans
• Landscape Pest Control
• - contact information, phone, email
• Gerald Hanswick
• 204-731-4426
• ger.hanswick@brelvanyard.com
• - "free estimates" somewhere on the page that is either led to by the eye, or very easy to notice and see
• - and my slogan which is "dependable, reliable, consistent"
• - room for a link to my future ratewell account so they can see reviews from real people
• - My Logo present
Nice to have
• Flowers or weeds depicted. Possibly some hardscaping and softscaping if it doesnt look too bulky and crowded.
Should not have
• grass

```html
<!DOCTYPE html>
<html lang="en">
<head>
<meta charset="utf-8">
<title>Marlow Landscaping</title>
<meta name="description" content="Marlow Landscaping: dependable, reliable, consistent. Hand weeding of perennial and flower beds, selective pruning, hedging, landscape construction and design, lawn treatment plans and landscape pest control.">
<link rel="stylesheet" href="https://fonts.googleapis.com/css2?family=Montserrat:wght@600;700&family=Open+Sans:wght@400;600;700&family=Raleway:wght@300;400;600&display=swap">
<style>
  :root {
    --yellow: #f7e81a;
    --yellow-deep: #e6d400;
    --ink: #1d1d1d;
    --text: #555555;
    --white: #ffffff;
    --panel: #eeeeee;
    --footer: #161616;
    --footer-line: #3a3a3a;
    --footer-text: #bdbdbd;
  }
  * { box-sizing: border-box; margin: 0; padding: 0; }
  html, body { width: 1200px; height: 2344px; overflow: hidden; background: var(--white); }
  body { position: relative; font-family: "Open Sans", Arial, sans-serif; color: var(--ink); }
  h1, h2, p { font-weight: 400; }

  /* Hero */
  .hero { position: absolute; left: 0; top: 0; width: 1200px; height: 668px; overflow: hidden; }
  .hero-photo {
    position: absolute; inset: 0;
    background:
      radial-gradient(ellipse 260px 200px at 220px 120px, rgba(150,140,120,.55), transparent 70%),
      radial-gradient(ellipse 200px 160px at 880px 540px, rgba(190,160,20,.55), transparent 70%),
      radial-gradient(ellipse 500px 300px at 700px 300px, rgba(90,110,50,.6), transparent 70%),
      linear-gradient(180deg, #3b3a2c 0%, #4a4a30 45%, #3d4a26 100%);
  }
  .hero-shade { position: absolute; inset: 0; background: rgba(20,20,15,.42); }
  .brand {
    position: absolute; top: 112px; left: 0; width: 1200px; text-align: center;
    font-family: "Montserrat", Arial, sans-serif; font-weight: 600; font-size: 62px;
    color: var(--white); letter-spacing: 1px; line-height: 1;
  }
  .brand-dot { display: inline-block; width: 50px; height: 50px; border-radius: 50%; background: var(--white); margin: 0 16px; vertical-align: -4px; }
  .welcome {
    position: absolute; top: 270px; left: 0; width: 1200px; text-align: center;
    font-family: "Raleway", Arial, sans-serif; font-weight: 300; font-size: 58px; color: var(--white); line-height: 1;
  }
  .welcome::before, .welcome::after {
    content: ""; display: inline-block; width: 176px; height: 2px; background: var(--yellow); vertical-align: 18px; margin: 0 6px;
  }
  .headline {
    position: absolute; top: 354px; left: 0; width: 1200px; text-align: center;
    font-family: "Raleway", Arial, sans-serif; font-size: 74px; color: var(--yellow); line-height: 1; letter-spacing: 1px;
  }
  .headline strong { font-family: "Montserrat", Arial, sans-serif; font-weight: 700; }
  .consult { position: absolute; top: 466px; left: 0; width: 1200px; display: flex; justify-content: center; align-items: center; gap: 32px; }
  .consult-label { font-family: "Raleway", Arial, sans-serif; font-size: 34px; color: var(--white); }
  .consult-icon { width: 70px; height: 70px; border: 2px solid var(--white); border-radius: 50%; display: flex; align-items: center; justify-content: center; }
  .consult-number { font-weight: 700; font-size: 46px; color: var(--white); margin-left: -12px; }
  .main-nav { position: absolute; top: 604px; left: 0; width: 1200px; height: 64px; border-top: 1px solid var(--yellow); display: flex; justify-content: center; align-items: center; gap: 54px; }
  .main-nav a { font-family: "Raleway", Arial, sans-serif; font-size: 19px; color: var(--white); text-decoration: none; text-transform: uppercase; }
  .main-nav a.is-active { color: var(--yellow); }

  .band { position: absolute; left: 0; width: 1200px; height: 8px; background: var(--yellow); }
  .pointer { position: absolute; left: 588px; width: 0; height: 0; border-left: 12px solid transparent; border-right: 12px solid transparent; border-top: 14px solid var(--yellow); }
  .drop-shadow { position: absolute; height: 60px; background: radial-gradient(ellipse 50% 60% at 50% 0%, rgba(0,0,0,.35), rgba(0,0,0,0) 100%); }

  /* About */
  .about-title { position: absolute; left: 80px; top: 736px; font-family: "Raleway", Arial, sans-serif; font-size: 44px; font-weight: 400; color: var(--ink); display: flex; align-items: center; gap: 28px; }
  .about-title::after { content: ""; width: 176px; height: 2px; background: var(--yellow-deep); }
  .about-text { position: absolute; left: 80px; top: 808px; width: 536px; font-size: 16.4px; line-height: 25px; color: var(--text); }
  .btn { position: absolute; background: var(--yellow); border: 1px solid #d8c800; border-radius: 4px; font-family: "Open Sans", Arial, sans-serif; color: var(--ink); display: flex; align-items: center; justify-content: center; text-transform: uppercase; text-decoration: none; }
  .btn-more { left: 78px; top: 1052px; width: 145px; height: 53px; font-size: 17px; }
  .about-photo { position: absolute; left: 680px; top: 760px; width: 360px; height: 330px; border-radius: 50%;
    background: radial-gradient(ellipse 50% 45% at 40% 35%, #78ad43 0%, rgba(120,173,67,.35) 60%, rgba(120,173,67,0) 80%),
                radial-gradient(ellipse 60% 35% at 75% 72%, #e4b59d 0%, rgba(228,181,157,0) 80%); }

  /* Estimate */
  .estimate { position: absolute; left: 77px; top: 1156px; width: 1045px; height: 200px; background: var(--panel); }
  .estimate-title { position: absolute; left: 45px; top: 48px; font-family: "Raleway", Arial, sans-serif; font-weight: 400; font-size: 42px; line-height: 52px; color: var(--ink); text-transform: uppercase; letter-spacing: 1px; }
  .field { position: absolute; width: 261px; height: 52px; background: var(--white); font-size: 15px; color: #444; padding: 15px 16px; }
  .btn-submit { left: 890px; top: 42px; width: 114px; height: 115px; font-weight: 700; font-size: 20px; }

  /* Services */
  .services-title { position: absolute; left: 0; top: 1418px; width: 1200px; text-align: center; font-family: "Raleway", Arial, sans-serif; font-weight: 400; font-size: 44px; line-height: 1.2; color: var(--ink); }
  .services-grid { position: absolute; left: 0; top: 1460px; width: 1200px; height: 540px; }
  .service-name { font-family: "Raleway", Arial, sans-serif; font-size: 25px; fill: var(--ink); }

  /* Footer */
  .site-footer { position: absolute; left: 0; top: 2083px; width: 1200px; height: 261px; background: var(--footer); }
  .footer-mark { position: absolute; left: 562px; top: 2040px; width: 76px; height: 76px; border-radius: 50%; background: var(--white); }
  .footer-nav { position: absolute; left: 80px; top: 31px; display: flex; gap: 36px; }
  .footer-nav a { font-size: 14px; color: var(--footer-text); text-decoration: none; text-transform: uppercase; }
  .footer-nav a.is-active { color: var(--white); }
  .social { position: absolute; right: 78px; top: 24px; display: flex; gap: 18px; align-items: center; }
  .social a { display: flex; align-items: center; gap: 7px; font-size: 14px; color: var(--white); text-decoration: none; }
  .social a::before { content: ""; width: 26px; height: 26px; border-radius: 50%; background: var(--white); }
  .footer-rule { position: absolute; left: 80px; top: 84px; width: 1042px; height: 1px; background: var(--footer-line); }
  .contact { position: absolute; top: 104px; display: flex; align-items: center; gap: 14px; color: var(--white); font-size: 14px; line-height: 19px; }
  .contact-icon { width: 46px; height: 46px; border-radius: 50%; background: var(--yellow); display: flex; align-items: center; justify-content: center; flex: none; }
  .contact strong { display: block; font-weight: 700; }
  .copyright { position: absolute; left: 0; top: 196px; width: 1200px; text-align: center; font-family: "Raleway", Arial, sans-serif; font-size: 14px; color: var(--footer-text); }
  .copyright strong { color: var(--yellow); font-weight: 600; }
  .footer-band { position: absolute; left: 0; bottom: 0; width: 1200px; height: 6px; background: var(--yellow); }
  .footer-pointer { position: absolute; left: 586px; bottom: 6px; width: 0; height: 0; border-left: 14px solid transparent; border-right: 14px solid transparent; border-bottom: 12px solid var(--yellow); }
</style>
</head>
<body>

<header class="hero" id="home">
  <div class="hero-photo" role="img" aria-label="Gloved hand pulling dandelion weeds from a garden bed"></div>
  <div class="hero-shade"></div>
  <div class="brand">MARLOW<span class="brand-dot"></span>LANDSCAPING</div>
  <h1 class="welcome">WELCOME TO</h1>
  <p class="headline"><strong>MARLOW</strong> LANDSCAPING</p>
  <div class="consult">
    <span class="consult-label">Call to Consult US</span>
    <span class="consult-icon">
      <svg width="34" height="34" viewBox="0 0 24 24"><path fill="#f7e81a" d="M6.6 10.8c1.4 2.8 3.8 5.1 6.6 6.6l2.2-2.2c.3-.3.7-.4 1-.2 1.1.4 2.3.6 3.6.6.6 0 1 .4 1 1V20c0 .6-.4 1-1 1C10.6 21 3 13.4 3 4c0-.6.4-1 1-1h3.5c.6 0 1 .4 1 1 0 1.3.2 2.5.6 3.6.1.3 0 .7-.2 1L6.6 10.8z"/></svg>
    </span>
    <span class="consult-number">204-731-4426</span>
  </div>
  <nav class="main-nav">
    <a class="is-active" href="#home">Home</a>
    <a href="#about">About</a>
    <a href="#services">Services</a>
    <a href="#contacts">Contacts</a>
  </nav>
</header>
<div class="band" style="top:668px"></div>
<div class="pointer" style="top:676px"></div>
<div class="drop-shadow" style="left:20px;top:676px;width:1160px"></div>

<section id="about">
  <h2 class="about-title">About</h2>
  <p class="about-text">Lorem Ipsum is simply dummy text of the printing and typesetting industry. Lorem Ipsum has been the industry's standard dummy text ever since the 1500s, when an unknown printer took a galley of type and scrambled it to make a type specimen book. It has survived not only five centuries, but also the leap into electronic typesetting, remaining essentially unchanged. It was popularised in the 1960s with the release of Letterline sheets containing Lorem Ipsum passages, and more recently with desktop publishing software like Folio PageSetter.</p>
  <a class="btn btn-more" href="#about">Read More</a>
  <div class="about-photo" role="img" aria-label="Hand holding a freshly pulled weed with roots and soil"></div>
</section>

<section class="estimate">
  <h2 class="estimate-title">Get a free<br>estimate</h2>
  <div class="field" style="left:337px;top:42px">Name</div>
  <div class="field" style="left:607px;top:42px">Phone</div>
  <div class="field" style="left:337px;top:105px">Email</div>
  <div class="field" style="left:607px;top:105px">Zipcode</div>
  <a class="btn btn-submit" href="#contacts">Submit</a>
</section>
<div class="band" style="top:1356px;left:77px;width:1045px;height:4px"></div>
<div class="pointer" style="top:1360px"></div>
<div class="drop-shadow" style="left:90px;top:1360px;width:1020px"></div>

<section id="services">
  <h2 class="services-title">Services</h2>
  <svg class="services-grid" viewBox="0 1460 1200 540" width="1200" height="540">
    <defs>
      <linearGradient id="tone-weeding" x1="0" y1="0" x2="1" y2="1"><stop offset="0" stop-color="#6b5a3e"/><stop offset="1" stop-color="#7f8a45"/></linearGradient>
      <linearGradient id="tone-pruning" x1="0" y1="0" x2="1" y2="1"><stop offset="0" stop-color="#b7d36a"/><stop offset="1" stop-color="#6d9a2e"/></linearGradient>
      <linearGradient id="tone-hedging" x1="0" y1="0" x2="0" y2="1"><stop offset="0" stop-color="#5f8a4a"/><stop offset="1" stop-color="#3e6a24"/></linearGradient>
      <linearGradient id="tone-construction" x1="0" y1="0" x2="0" y2="1"><stop offset="0" stop-color="#c9b7a8"/><stop offset="1" stop-color="#6c8f3e"/></linearGradient>
      <linearGradient id="tone-design" x1="0" y1="0" x2="1" y2="1"><stop offset="0" stop-color="#9cbf8c"/><stop offset="1" stop-color="#d9c69a"/></linearGradient>
      <linearGradient id="tone-pest" x1="0" y1="0" x2="1" y2="1"><stop offset="0" stop-color="#8fb04a"/><stop offset="1" stop-color="#4f6e2a"/></linearGradient>
      <linearGradient id="tone-lawn" x1="0" y1="0" x2="1" y2="1"><stop offset="0" stop-color="#d4ea3a"/><stop offset="1" stop-color="#a8cc22"/></linearGradient>
    </defs>
    <g stroke="#f3e21a" stroke-width="3">
      <g role="img" aria-label="Weeding of Perennial and Flower Beds: hands pulling weeds from a bed"><title>Weeding of Perennial and Flower Beds</title><polygon fill="url(#tone-weeding)" points="202.5,1467 327.5,1539 327.5,1683 202.5,1755 77.5,1683 77.5,1539"/></g>
      <g role="img" aria-label="Selective Pruning of Trees and Shrubs: secateurs cutting a branch"><title>Selective Pruning of Trees and Shrubs</title><polygon fill="url(#tone-pruning)" points="467.5,1467 592.5,1539 592.5,1683 467.5,1755 342.5,1683 342.5,1539"/></g>
      <g role="img" aria-label="Hedging: trimmer shaping a hedge"><title>Hedging</title><polygon fill="url(#tone-hedging)" points="732.5,1467 857.5,1539 857.5,1683 732.5,1755 607.5,1683 607.5,1539"/></g>
      <g role="img" aria-label="Landscape Construction: stone path and garden fountain"><title>Landscape Construction</title><polygon fill="url(#tone-construction)" points="997.5,1467 1122.5,1539 1122.5,1683 997.5,1755 872.5,1683 872.5,1539"/></g>
      <g role="img" aria-label="Landscape Design: garden plan drawing"><title>Landscape Design</title><polygon fill="url(#tone-design)" points="335,1697 460,1769 460,1913 335,1985 210,1913 210,1769"/></g>
      <g role="img" aria-label="Landscape Pest Control: spraying garden shrubs"><title>Landscape Pest Control</title><polygon fill="url(#tone-pest)" points="865,1697 990,1769 990,1913 865,1985 740,1913 740,1769"/></g>
    </g>
    <polygon fill="url(#tone-lawn)" stroke="#111111" stroke-width="4" points="600,1697 725,1769 725,1913 600,1985 475,1913 475,1769"/>
    <text class="service-name" x="600" y="1845" text-anchor="middle">Total Lawn</text>
    <text class="service-name" x="600" y="1875" text-anchor="middle">Treatment Plans</text>
    <circle cx="600" cy="1920" r="20" fill="none" stroke="#111111" stroke-width="1.5"/>
    <path d="M596 1912 L604 1920 L596 1928" fill="none" stroke="#111111" stroke-width="2"/>
  </svg>
</section>

<footer class="site-footer" id="contacts">
  <nav class="footer-nav">
    <a class="is-active" href="#home">Home</a>
    <a href="#services">Services</a>
    <a href="#about">About</a>
    <a href="#contacts">Contact</a>
  </nav>
  <div class="social">
    <a href="#contacts">Circlebook</a>
    <a href="#contacts">Chirper</a>
    <a href="#contacts">Ratewell</a>
    <a href="#contacts">Snapframe</a>
  </div>
  <div class="footer-rule"></div>
  <div class="contact" style="left:78px">
    <span class="contact-icon"><svg width="20" height="22" viewBox="0 0 24 24"><path fill="#111" d="M12 2a7 7 0 0 0-7 7c0 5.2 7 13 7 13s7-7.8 7-13a7 7 0 0 0-7-7zm0 9.5A2.5 2.5 0 1 1 12 6.5a2.5 2.5 0 0 1 0 5z"/></svg></span>
    <span><strong>POSTAL ADDRESS</strong>123 Building Name, City, Country - zipcode</span>
  </div>
  <div class="contact" style="left:516px">
    <span class="contact-icon"><svg width="20" height="20" viewBox="0 0 24 24"><path fill="#111" d="M6.6 10.8c1.4 2.8 3.8 5.1 6.6 6.6l2.2-2.2c.3-.3.7-.4 1-.2 1.1.4 2.3.6 3.6.6.6 0 1 .4 1 1V20c0 .6-.4 1-1 1C10.6 21 3 13.4 3 4c0-.6.4-1 1-1h3.5c.6 0 1 .4 1 1 0 1.3.2 2.5.6 3.6.1.3 0 .7-.2 1L6.6 10.8z"/></svg></span>
    <span>204-731-4426</span>
  </div>
  <div class="contact" style="left:789px">
    <span class="contact-icon"><svg width="22" height="18" viewBox="0 0 24 20"><rect x="1" y="2" width="22" height="16" rx="2" fill="#111"/><path d="M2 4l10 7 10-7" fill="none" stroke="#f7e81a" stroke-width="1.6"/></svg></span>
    <span>ger.hanswick@brelvanyard.com</span>
  </div>
  <p class="copyright">© <strong>MARLOW LANDSCAPING</strong> &nbsp;- 2017. All Rights Reserved.</p>
  <div class="footer-pointer"></div>
  <div class="footer-band"></div>
</footer>
<div class="footer-mark"></div>

</body>
</html>
```